Thistle Croft B&B Business Card

This beautiful high-class B&B is looking for a business card that stands out from the rest. They are in the middle of the countryside, have chickens, geese and a dog. They also love bumble bees.

I was maybe thinking a rustic drawing / print of a bumble bee and a sketch of the house, I am not sure.. I quite like the feel of this... http://www.fenwick-mill.co.uk/

Industry/Entity Type

Business

Contact Information for Business Card

Thistle Croft
Bed & Breakfast
Holtwick, Marrowby, Westshire, MB4 7QR
01632 961847 | www.thistlecroft.co.uk

```html
<!DOCTYPE html>
<html lang="en">
<head>
<meta charset="utf-8">
<title>Thistle Croft B&amp;B Business Card</title>
<link rel="stylesheet" href="https://fonts.googleapis.com/css2?family=Cinzel:wght@400&family=Oranienbaum&display=swap">
<style>
  :root {
    --bg: #e4e2e0;
    --card: #ffffff;
    --ink: #9a7f76;
    --frame: #c9ad9f;
    --scene-stone: #ebe4da;
    --scene-roof: #c9a69a;
    --scene-grass: #8d8c6e;
    --scene-path: #e6ddd6;
    --hens: #a4958a;
  }
  * { margin: 0; padding: 0; box-sizing: border-box; }
  html, body { width: 1200px; height: 1200px; overflow: hidden; background: var(--bg); }
  .card {
    position: absolute; left: 156px; width: 888px; height: 528px;
    background: var(--card); overflow: hidden;
  }
  .card--front { top: 55px; }
  .card--back { top: 608px; }

  .scene { position: absolute; }
  .scene--front {
    left: 0; top: 0; width: 480px; height: 528px;
    background:
      linear-gradient(90deg, rgba(255,255,255,0) 55%, #fff 100%),
      linear-gradient(180deg, #f4f1ee 0%, var(--scene-stone) 28%, var(--scene-roof) 40%, var(--scene-stone) 52%, var(--scene-path) 72%, var(--scene-grass) 100%);
  }
  .scene--back-left, .scene--back-right {
    top: 0; width: 230px; height: 528px;
    background: linear-gradient(180deg, #fbf9f7 0%, #efe8e2 22%, var(--scene-stone) 45%, #dfe2d4 58%, var(--scene-path) 75%, var(--scene-grass) 100%);
  }
  .scene--back-left { left: 0; -webkit-mask-image: linear-gradient(90deg, #000 20%, transparent 100%); mask-image: linear-gradient(90deg, #000 20%, transparent 100%); }
  .scene--back-right { right: 0; -webkit-mask-image: linear-gradient(270deg, #000 20%, transparent 100%); mask-image: linear-gradient(270deg, #000 20%, transparent 100%); }

  .nameplate { position: absolute; border: 1px solid var(--frame); color: var(--ink); }
  .nameplate__name {
    position: absolute; font-family: "Cinzel", serif; font-weight: 400; line-height: 0.98; letter-spacing: 0.02em;
  }
  .nameplate__line { display: flex; align-items: baseline; white-space: nowrap; }
  .nameplate__sub { font-family: "Oranienbaum", serif; letter-spacing: 0; }

  .card--front .nameplate { left: 356px; top: 163px; width: 476px; height: 199px; }
  .card--front .nameplate__name { left: 30px; top: 26px; font-size: 68px; }
  .card--front .nameplate__line { gap: 16px; }
  .card--front .nameplate__sub { font-size: 32px; }

  .card--back .nameplate { left: 280px; top: 58px; width: 328px; height: 132px; }
  .card--back .nameplate__name { left: 28px; top: 14px; font-size: 44px; }
  .card--back .nameplate__line { gap: 10px; }
  .card--back .nameplate__sub { font-size: 21px; }

  .contact {
    position: absolute; left: 0; width: 100%; text-align: center;
    font-family: "Oranienbaum", serif; color: var(--ink);
  }
  .contact--address { top: 212px; font-size: 23px; line-height: 30px; }
  .contact--phone { top: 272px; font-size: 27px; }
  .contact--web { top: 448px; font-size: 22px; }

  .hens {
    position: absolute; left: 368px; top: 336px; width: 152px; height: 96px;
    background: radial-gradient(ellipse at center, var(--hens) 0%, rgba(164,149,138,0.5) 45%, rgba(255,255,255,0) 72%);
  }
</style>
</head>
<body>
  <section class="card card--front">
    <div class="scene scene--front" role="img" aria-label="Soft sketched drawing of the stone croft house with tiled roof, garden and gravel drive"></div>
    <div class="nameplate">
      <div class="nameplate__name">
        <div class="nameplate__line">Thistle</div>
        <div class="nameplate__line">Croft <span class="nameplate__sub">Bed &amp; Breakfast</span></div>
      </div>
    </div>
  </section>

  <section class="card card--back">
    <div class="scene scene--back-left" role="img" aria-label="Faded sketch of the house and drive"></div>
    <div class="scene scene--back-right" role="img" aria-label="Faded sketch of the house and drive"></div>
    <div class="nameplate">
      <div class="nameplate__name">
        <div class="nameplate__line">Thistle</div>
        <div class="nameplate__line">Croft <span class="nameplate__sub">Bed &amp; Breakfast</span></div>
      </div>
    </div>
    <p class="contact contact--address">Holtwick, Marrowby, Westshire,<br>MB4 7QR</p>
    <p class="contact contact--phone">01632 961847</p>
    <div class="hens" role="img" aria-label="Small sketch of two hens"></div>
    <p class="contact contact--web">www.thistlecroft.co.uk</p>
  </section>
</body>
</html>
```